Webdesign für Ingenieurbüro
Zielgruppe
Ingenieurbüro Varnotek GmbH
Leistungen:
Siedlungswasserwirtschaft
Straßen- und Ingenieurbau
Hochwasserschutz / Wasserbau
Pegelanlagen
Komplexerschließungen
Koordinierung nach BaustellV
Landschaftsbau
Zielgruppe ist die Öffentliche Hand
Aufgabenstellung
Leistungsbereiche und Stellenangebote (zZt. 3 Stück) sollen zu gleichen Teilen im Fokus stehen. Call to action zum Berweberformular ist nötig.
Zu beachten wäre, dass das Unternehmen für öffentliche Auftraggeber arbeitet. Die Seite sollte klar strukturiert und seriös wirken.
Der Login-Bereich soll in den Hintergrund treten, eventuell über dem footer.
Logo aus dem Cover - siehe anbei übernehmen

```html
<!DOCTYPE html>
<html lang="de">
<head>
<meta charset="utf-8">
<title>Ingenieurbüro Varnotek GmbH</title>
<link href="https://fonts.googleapis.com/css2?family=Lato:wght@400;700;900&display=swap" rel="stylesheet">
<style>
:root{
  --navy:#0b3c94;
  --navy-deep:#0b2a6b;
  --bright:#0a97dd;
  --heading:#1b4f9c;
  --pale:#eaf4fb;
  --text:#222;
  --white:#fff;
}
*{box-sizing:border-box;margin:0;padding:0}
html,body{width:1200px;height:2700px;overflow:hidden}
body{font-family:'Lato',sans-serif;color:var(--text);background:var(--white);position:relative}
.abs{position:absolute}

/* nav */
.topbar{left:0;top:0;width:1200px;height:54px;background:var(--navy)}
.nav{right:120px;top:0;height:54px;display:flex;gap:44px;align-items:center}
.nav a{color:var(--white);text-decoration:none;font-size:14px}

/* hero */
.hero{left:0;top:54px;width:1200px;height:471px;background:linear-gradient(90deg,#eef6fc 0%,#d8ebf8 28%,#8aa2a0 52%,#6f7f6a 75%,#a9a39a 100%)}
.brand{left:120px;top:70px;display:flex;align-items:center;gap:12px}
.brand-mark{width:22px;height:22px;background:var(--navy)}
.brand-name{font-size:22px;font-weight:700;color:var(--navy);line-height:1.1}
.hero-title{left:118px;top:316px;font-size:39px;font-weight:900;color:var(--navy);line-height:46px;letter-spacing:-1px}
.hero-sub{left:119px;top:422px;width:470px;height:29px;background:var(--bright);color:var(--white);font-size:17px;padding:3px 12px}
.contact-form{left:956px;top:141px;width:244px;height:308px;background:var(--bright);padding:28px 21px 0 28px}
.contact-form h3{color:var(--white);font-size:15px;font-weight:700;line-height:18px;margin-bottom:16px}
.field{background:var(--white);height:28px;margin-bottom:7px;font-size:10px;color:#666;padding:8px 11px}
.field.tall{height:63px}
.send{background:var(--navy);color:var(--white);height:28px;font-size:12px;font-weight:700;text-align:center;line-height:28px}

/* welcome */
.welcome{left:0;top:525px;width:1200px;height:283px;background:var(--pale);border-bottom:1px solid #d6e4ef}
.sec-h{font-size:28px;color:var(--heading);font-weight:400}
.welcome h2{left:120px;top:50px}
.welcome p{top:103px;width:330px;font-size:12.5px;line-height:22.5px}
.photo-frame{left:858px;top:50px;width:215px;height:160px;background:var(--white);padding:9px;transform:rotate(-6deg);box-shadow:0 3px 10px rgba(0,0,0,.2)}
.photo-frame div{width:100%;height:100%;background:linear-gradient(180deg,#b9cde0,#e8eef3 55%,#8d9398)}

/* services */
.services-h{left:0;width:1200px;top:858px;text-align:center}
.card{width:210px;height:157px;background:var(--white);box-shadow:0 2px 10px rgba(0,0,0,.08);text-align:center}
.card svg{position:absolute;left:75px;top:26px}
.card .rule{position:absolute;left:24px;right:24px;top:110px;border-top:1px solid #ddd}
.card .label{position:absolute;left:0;right:0;top:119px;font-size:13.5px;line-height:16px;color:#333}
.card.single .label{top:127px}
.card.active{background:var(--bright)}
.card.active .label{color:var(--white);font-weight:700}
.card.active .rule{border-color:rgba(255,255,255,.4)}

/* jobs */
.jobs-photo{left:0;top:1348px;width:600px;height:361px;background:linear-gradient(135deg,#a98a78 0%,#e0b48a 35%,#6b6f78 70%,#2e3440 100%)}
.jobs{left:600px;top:1348px;width:600px;height:361px;background:var(--bright);color:var(--white);padding:70px 0 0 42px}
.jobs h2{font-size:21px;font-weight:700;margin-bottom:24px}
.jobs .lead{font-size:12.5px;font-weight:700;margin-bottom:18px}
.jobs li{list-style:none;font-size:13px;line-height:22.5px}
.jobs li::before{content:"›";margin-right:10px}
.apply{display:inline-block;margin-top:26px;border:2px solid var(--white);width:153px;height:36px;line-height:32px;text-align:center;font-size:13px;font-weight:700}

/* projects */
.projects-h{left:0;width:1200px;top:1755px;text-align:center}
.project{top:1823px;width:301px;height:205px}
.project .img{height:175px}
.project .cap{height:30px;background:var(--navy);color:var(--white);font-size:13.5px;font-weight:700;padding:6px 12px}
.chev{top:1902px}

/* news */
.news{left:0;top:2086px;width:1200px;height:362px;background:var(--pale)}
.news h2{left:120px;top:95px}
.news-img{left:120px;top:150px;width:366px;height:166px;background:linear-gradient(180deg,#5b6658 0%,#8e968d 40%,#c9d2d6 70%,#7d8478 100%)}
.pager{top:39px;width:27px;height:30px;background:var(--navy)}
.pager svg{margin:8px 0 0 8px}
.news-card{width:267px;height:107px;background:var(--white);box-shadow:0 2px 8px rgba(0,0,0,.08);padding:18px 20px}
.news-card .date{font-size:11.5px;font-weight:700;color:var(--navy);margin-bottom:6px}
.news-card p{font-size:11px;line-height:18px}

/* login */
.login{left:0;top:2448px;width:1200px;height:121px;background:linear-gradient(90deg,#0c4fb3,#0a64c8 60%,#1a8ad8)}
.login h3{left:336px;top:20px;font-size:19px;font-weight:700;color:var(--white)}
.input{top:47px;width:266px;height:36px;background:var(--white);font-size:12px;padding:10px 12px}
.login-btn{left:902px;top:47px;width:178px;height:36px;background:var(--navy);color:var(--white);font-size:13px;font-weight:700;text-align:center;line-height:36px}
.forgot{right:121px;top:91px;font-size:11.5px;font-weight:700;color:var(--white)}

/* footer */
.footer{left:0;top:2569px;width:1200px;height:131px;background:var(--navy-deep);color:var(--white)}
.footer .col{top:46px;font-size:10.5px;line-height:18px}
.footer strong{font-size:12.5px}
.divider{top:40px;height:52px;border-left:1px solid rgba(255,255,255,.35)}
.social{right:120px;top:62px;display:flex;gap:21px}
.social span{width:14px;height:14px;border-radius:50%;background:var(--white)}
</style>
</head>
<body>

<div class="abs topbar"></div>
<nav class="abs nav"><a>Home</a><a>Stellenangebote</a><a>Leistungen</a><a>Unternehmen</a><a>Projekte</a><a>Kontakt</a></nav>

<section class="abs hero" role="img" aria-label="Foto eines ausgebauten Bachlaufs mit Steinufer und Brücke"></section>
<div class="abs brand"><span class="brand-mark"></span><span class="brand-name">Ingenieurbüro<br>Varnotek GmbH</span></div>
<h1 class="abs hero-title">Über 25 Jahre Ingenieurbüro<br>VARNOTEK GmbH</h1>
<div class="abs hero-sub">Ingenieurleistungen aus Musterstadt-Nord seit 1994</div>

<form class="abs contact-form">
  <h3>Excepteur sint occaecat cupidatat non proident</h3>
  <div class="field">Name</div>
  <div class="field">Email</div>
  <div class="field">Telefon</div>
  <div class="field tall">Kommentare</div>
  <div class="send">SENDEN</div>
</form>

<section class="abs welcome">
  <h2 class="abs sec-h">Herzlich willkommen</h2>
  <p class="abs" style="left:120px">Willkommen bei der Ingenieurbüro Varnotek GmbH, einem mittelständischen Unternehmen, welches 1994 gegründet wurde. Wir sind ein zuverlässiger Partner für fachgerechte Beratung, Planung und Bauüberwachung von Maßnahmen des Tief-, Wasser- und Straßenbaues.</p>
  <p class="abs" style="left:507px;width:320px">Hierfür sind 18 hochqualifizierte und engagierte Ingenieure und technische Mitarbeiter verantwortlich. Moderne Kommunikationstechnik und Spezialsoftware, sowie die Kreativität der Mitarbeiter sind ein Garant für effektive Lösungen.</p>
  <div class="abs photo-frame"><div role="img" aria-label="Foto des Bürogebäudes"></div></div>
</section>

<h2 class="abs sec-h services-h">Leistungen</h2>

<div class="abs card" style="left:120px;top:931px">
  <svg width="60" height="60" viewBox="0 0 60 60" fill="none" stroke="#0a97dd" stroke-width="2"><path d="M24 6C16 18 10 26 10 34a14 14 0 0 0 20 12"/><circle cx="36" cy="32" r="7" stroke="#0b3c94"/><circle cx="36" cy="32" r="13" stroke="#0b3c94" stroke-dasharray="4 3"/></svg>
  <div class="rule"></div><div class="label">Siedlungswasser-<br>wirtschaft</div>
</div>
<div class="abs card active" style="left:370px;top:931px">
  <svg width="60" height="60" viewBox="0 0 60 60" fill="none" stroke="#fff" stroke-width="2"><circle cx="30" cy="28" r="30" fill="rgba(255,255,255,.2)" stroke="none"/><path d="M16 30a14 14 0 0 1 28 0M12 31h36M22 36a8 8 0 0 0 16 0"/><path d="M27 16v8M33 16v8"/></svg>
  <div class="rule"></div><div class="label">Straßen- und<br>Ingenieurbau</div>
</div>
<div class="abs card" style="left:619px;top:931px">
  <svg width="60" height="60" viewBox="0 0 60 60" fill="none" stroke="#0b3c94" stroke-width="2"><path d="M10 30L28 14l18 16M14 27v15h28V27"/><path d="M24 42v-9h8v9"/><path d="M6 48c4-3 8 3 12 0s8 3 12 0 8 3 12 0 8 3 12 0" stroke="#0a97dd"/><circle cx="42" cy="16" r="6"/><path d="M39 16l2 2 4-4"/></svg>
  <div class="rule"></div><div class="label">Hochwasserschutz /<br>Wasserbau</div>
</div>
<div class="abs card single" style="left:869px;top:931px">
  <svg width="60" height="60" viewBox="0 0 60 60" fill="none" stroke="#0b3c94" stroke-width="6"><path d="M12 46a22 22 0 1 1 36 0"/><path d="M30 40l8-12" stroke="#0a97dd" stroke-width="3"/></svg>
  <div class="rule"></div><div class="label">Pegelanlagen</div>
</div>
<div class="abs card single" style="left:370px;top:1126px">
  <svg width="60" height="60" viewBox="0 0 60 60" fill="none" stroke="#0b3c94" stroke-width="2"><rect x="10" y="8" width="40" height="40"/><path d="M10 28h40M30 8v40M14 12l32 32M46 12L14 44"/><path d="M4 54h52" stroke="#0a97dd"/></svg>
  <div class="rule"></div><div class="label">Komplexerschließungen</div>
</div>
<div class="abs card" style="left:619px;top:1126px">
  <svg width="60" height="60" viewBox="0 0 60 60" fill="none" stroke="#0b3c94" stroke-width="2"><circle cx="30" cy="26" r="7"/><path d="M20 46a10 10 0 0 1 20 0"/><circle cx="12" cy="12" r="5"/><rect x="43" y="7" width="10" height="12"/><circle cx="48" cy="44" r="5"/><path d="M16 16l8 5M43 18l-7 4M44 41l-8-6" stroke="#0a97dd"/></svg>
  <div class="rule"></div><div class="label">Koordinierung nach<br>BaustellV</div>
</div>

<div class="abs jobs-photo" role="img" aria-label="Foto eines gelben Schutzhelms auf Solarmodulen im Gegenlicht"></div>
<section class="abs jobs">
  <h2>Stellenangebote</h2>
  <p class="lead">Wir haben aktuell Stellenangebote aus den folgenden Bereichen:</p>
  <ul><li>Hydrologie</li><li>Wasserwirtschaft</li><li>Verkehrsanlagen</li></ul>
  <div class="apply">›&nbsp; Jetzt bewerben</div>
</section>

<h2 class="abs sec-h projects-h">Projekte</h2>
<svg class="abs chev" style="left:74px" width="20" height="36" viewBox="0 0 20 36" fill="none" stroke="#0a97dd" stroke-width="3"><path d="M18 2L3 18l15 16"/></svg>
<div class="abs project" style="left:120px"><div class="img" role="img" aria-label="Foto einer Kanalbaustelle" style="background:linear-gradient(160deg,#8a9a7c,#b7b0a4 50%,#5d5e56)"></div><div class="cap">›&nbsp; Siedlungswasserwirtschaft</div></div>
<div class="abs project" style="left:450px"><div class="img" role="img" aria-label="Foto von Asphaltarbeiten auf einer Straße" style="background:linear-gradient(170deg,#cfd6dc,#7f8b74 45%,#54575b)"></div><div class="cap">›&nbsp; Straßen- und Ingenieurbau</div></div>
<div class="abs project" style="left:779px"><div class="img" role="img" aria-label="Foto eines begrünten Deichs" style="background:linear-gradient(180deg,#6f8fc0,#c9d6e6 40%,#5c7a38 60%,#3e5a26)"></div><div class="cap">›&nbsp; Hochwasserschutz / Wasserbau</div></div>
<svg class="abs chev" style="left:1106px" width="20" height="36" viewBox="0 0 20 36" fill="none" stroke="#0a97dd" stroke-width="3"><path d="M2 2l15 16L2 34"/></svg>

<section class="abs news">
  <h2 class="abs sec-h">News</h2>
  <div class="abs news-img" role="img" aria-label="Foto eines Flusslaufs mit Steinböschung"></div>
  <div class="abs pager" style="left:1025px"><svg width="11" height="14" viewBox="0 0 11 14" fill="none" stroke="#fff" stroke-width="2"><path d="M8 1L2 7l6 6"/></svg></div>
  <div class="abs pager" style="left:1053px"><svg width="11" height="14" viewBox="0 0 11 14" fill="none" stroke="#fff" stroke-width="2"><path d="M3 1l6 6-6 6"/></svg></div>
  <div class="abs news-card" style="left:528px;top:85px;padding-left:35px"><div class="date">17.05.-21.05.2010</div><p>Qualifizierung zum Sicherheits- und Gesundheitsschutz-Koordinator gemäß Anlagen B &amp; C zur RAB 30 in Neuss</p></div>
  <div class="abs news-card" style="left:811px;top:85px;padding-top:16px"><div class="date">28.01.2010</div><p>Fachseminar über den Schutz hydraulischer Systeme vor Luftansammlungen, Unterdruck/Vakuum und dynamischen Druckänderungen in Chemnitz</p></div>
  <div class="abs news-card" style="left:528px;top:209px;padding-top:28px"><div class="date">20.11.2009</div><p>Seminar Vertragsgestaltung und Abrechnung nach der neuen HOAI in Dresden</p></div>
  <div class="abs news-card" style="left:811px;top:209px"><div class="date">07.10.2009</div><p>Fortbildung mit ausgewählten Themen aus Straßenplanung und Straßenentwurf in Dresden</p></div>
</section>

<section class="abs login">
  <svg class="abs" style="left:120px;top:15px" width="110" height="92" viewBox="0 0 110 92" fill="none" stroke="#fff" stroke-width="2.5" opacity=".9"><circle cx="26" cy="22" r="20"/><path d="M4 88V72a22 22 0 0 1 44 0v12z"/><rect x="52" y="42" width="46" height="36" rx="4" transform="rotate(-12 75 60)" stroke="#5fb4ee"/><path d="M62 42v-8a12 12 0 0 1 24-4v8" stroke="#5fb4ee"/><circle cx="76" cy="60" r="4" stroke="#5fb4ee"/></svg>
  <h3 class="abs">Interner Bereich</h3>
  <div class="abs input" style="left:336px">Kundennummer</div>
  <div class="abs input" style="left:619px">Passwort</div>
  <div class="abs login-btn">LOGIN</div>
  <div class="abs forgot">Passwort vergessen?</div>
</section>

<footer class="abs footer">
  <div class="abs col" style="left:120px;top:45px"><strong>Ingenieurbüro Varnotek GmbH</strong><br>Ahornweg 12<br>09999 Musterstadt</div>
  <div class="abs divider" style="left:395px"></div>
  <div class="abs col" style="left:515px;top:40px">Tel.&nbsp;&nbsp; 0123 / 45678-0<br>Fax:&nbsp;&nbsp; 0123 / 45678-43<br>Email : info@varnotek-beispiel.de</div>
  <div class="abs divider" style="left:804px"></div>
  <div class="abs social"><span></span><span></span><span></span><span></span><span></span></div>
</footer>

</body>
</html>
```